Woo Commerce Redesign

We have a website--www.lessonharborbooks.com (a woocommerce theme on Word Press) and are looking for someone to customize the design for us so it is better optimized, more intuitive and has a nicer look and feel.

The only design element we need to keep is the logo.

Our primary aim is to get the value proposition at the top of the page. I am thinking this means that we need to design the header but we will accept better options as well.

Our three-fold value prop is:
Price Match Guarantee
*Free Shipping
Same Day Service

*free shipping is on orders over $45

Internal Category Pages:
We also need to design an internal landing page template optimized for both computer and mobile users so that when an individual clicks on an ad, they come to a page that answers those important questions of who are they? Why should I buy from them? and what do they offer?

We expect this copy to be something like the following:
“Welcome to Lesson Harbor, your one stop place for [math curriculum] for both schools and homeschoolers.
Our price match guarantee, free shipping and same day service make us the perfect partner for all of your curriculum needs!
Click here to see all of our [math] titles for grades 1-12 or select the grade you are looking for and you will find all of the available [math] products.

Reason: I am extending this deadline because I did not get feedback to the designers over the weekend. I will provide feedback in the next few days so we can get a final design.

```html
<!DOCTYPE html>
<html lang="en">
<head>
<meta charset="utf-8">
<title>About Lesson Harbor</title>
<link rel="stylesheet" href="https://fonts.googleapis.com/css2?family=Mulish:wght@400;600&family=Open+Sans:wght@400;600;700&display=swap">
<style>
:root{
  --stage:#eef0f3;
  --white:#ffffff;
  --brand-blue:#1351a8;
  --deep-blue:#0f3d99;
  --navy:#0f2c72;
  --heading-blue:#1d3f8e;
  --orange:#e85d1e;
  --text-grey:#6b6b6b;
  --dark-text:#333333;
  --card-line:#d6d6d6;
  --old-price:#8a8a8a;
}
*{box-sizing:border-box;margin:0;padding:0}
html,body{width:1200px;height:2659px;overflow:hidden;background:var(--stage)}
body{font-family:"Open Sans",sans-serif;position:relative}
h1,h2{font-weight:400}
.screen{position:absolute;left:197px;top:0;width:806px;height:2659px;background:var(--white);overflow:hidden}

.site-header{height:119px;display:flex;align-items:center;justify-content:space-between;padding:0 48px 0 48px}
.brand{display:flex;align-items:center;gap:14px}
.brand-mark{width:22px;height:22px;background:var(--orange)}
.brand-name{font-family:"Open Sans",sans-serif;font-weight:700;font-size:40px;color:var(--heading-blue);letter-spacing:-0.5px}
.header-tools{display:flex;align-items:center;gap:34px}

.value-bar{height:67px;background:var(--brand-blue);display:flex;align-items:center;justify-content:space-between;padding:0 28px;color:var(--white);font-size:21px}
.value-item{display:flex;align-items:center;gap:8px}

.hero{height:280px;position:relative;background:linear-gradient(100deg,#3b2a20 0%,#6a4f3c 35%,#8a7766 60%,#5d5650 100%);display:flex;align-items:center;justify-content:center}
.hero-title{border:2px solid rgba(255,255,255,.85);width:258px;height:56px;display:flex;align-items:center;justify-content:center;font-family:"Mulish",sans-serif;font-weight:600;font-size:36px;color:var(--white);letter-spacing:0.5px}

.about{text-align:center;padding-top:50px}
.about-title{font-family:"Mulish",sans-serif;font-weight:400;font-size:40px;color:var(--heading-blue)}
.about-rule{width:170px;height:2px;background:var(--orange);margin:14px auto 0;position:relative}
.about-rule::after{content:"";position:absolute;left:60px;top:-2px;width:50px;height:5px;background:var(--orange)}
.about-copy{width:620px;margin:36px auto 0;font-size:23px;line-height:35px;color:var(--text-grey)}

.latest{margin-top:90px}
.section-title{display:flex;align-items:center;justify-content:center;gap:18px;font-family:"Mulish",sans-serif;font-weight:400;font-size:32px;color:var(--orange)}
.section-title .flourish{width:70px;height:2px;background:var(--orange);position:relative}
.section-title .flourish::after{content:"";position:absolute;top:-4px;width:10px;height:10px;border-radius:50%;background:var(--orange)}
.flourish.left::after{right:0}
.flourish.right::after{left:0}

.product-grid{display:grid;grid-template-columns:272px 272px;gap:22px 14px;padding:0 0 0 81px;margin-top:26px}
.product-card{height:330px;border:2px solid var(--card-line);box-shadow:0 2px 4px rgba(0,0,0,.12);display:flex;flex-direction:column;align-items:center;padding-top:36px}
.product-cover{width:134px;height:130px;box-shadow:2px 3px 6px rgba(0,0,0,.3)}
.cover-a{background:linear-gradient(135deg,#8a5a3a,#c9b79a 60%,#7c2f3c)}
.cover-b{background:linear-gradient(135deg,#3d2a1c,#8c6a4a 55%,#2a3a5a)}
.cover-c{background:linear-gradient(135deg,#2c3c7a,#a07a5a 50%,#b83a3a)}
.cover-d{background:linear-gradient(135deg,#7a2a2a,#c9a46a 50%,#2c3c6a)}
.product-name{margin-top:20px;font-size:17px;line-height:25px;color:var(--dark-text);text-align:center;width:210px}
.price-row{display:flex;align-items:center;gap:12px;margin-top:16px}
.price-old{font-size:16px;color:var(--old-price);text-decoration:line-through}
.price-new{font-size:21px;color:var(--heading-blue)}
.buy-button{width:106px;height:34px;border:2px solid var(--orange);border-radius:17px;color:var(--orange);font-size:14px;font-weight:600;display:flex;align-items:center;justify-content:center}

.newsletter{position:absolute;top:1912px;left:0;width:806px;height:146px;background:var(--orange);text-align:center;padding-top:20px}
.newsletter-title{font-family:"Mulish",sans-serif;font-weight:400;font-size:28px;color:var(--white)}
.newsletter-form{display:flex;justify-content:center;margin-top:14px}
.email-field{width:356px;height:42px;background:var(--white);font-size:16px;color:var(--dark-text);display:flex;align-items:center;padding-left:22px}
.subscribe-button{width:142px;height:42px;background:var(--navy);color:var(--white);font-size:19px;font-weight:600;display:flex;align-items:center;justify-content:center}

.quick-links{position:absolute;top:2058px;left:0;width:806px;height:58px;background:var(--deep-blue);display:grid;grid-template-columns:168px 143px 160px 335px}
.quick-link{display:flex;align-items:center;justify-content:center;border-right:1px solid rgba(255,255,255,.25)}
.quick-link:last-child{border-right:none;justify-content:flex-start;padding-left:60px}

.site-footer{position:absolute;top:2116px;left:0;width:806px;height:543px;background:var(--brand-blue);text-align:center;padding-top:34px}
.social-row{display:flex;justify-content:center;gap:12px}
.social-dot{width:36px;height:36px;border-radius:50%;background:#0b2a66}
.payment-row{display:flex;justify-content:center;gap:12px;margin-top:16px}
.payment-card{width:38px;height:23px;border-radius:3px;background:#e8ecf3}
.copyright{margin-top:22px;font-size:16px;color:#d7e1f2}
</style>
</head>
<body>
<div class="screen">
  <header class="site-header">
    <div class="brand"><span class="brand-mark"></span><span class="brand-name">Lesson Harbor</span></div>
    <div class="header-tools">
      <svg width="40" height="40" viewBox="0 0 40 40" aria-label="Search"><circle cx="16" cy="16" r="11" fill="none" stroke="#8a8a8a" stroke-width="5"/><line x1="24" y1="24" x2="36" y2="36" stroke="#8a8a8a" stroke-width="6" stroke-linecap="round"/></svg>
      <svg width="78" height="40" viewBox="0 0 78 40" aria-label="Menu"><rect y="2" width="78" height="6" fill="#8a8a8a"/><rect y="17" width="78" height="6" fill="#8a8a8a"/><rect y="32" width="78" height="6" fill="#8a8a8a"/></svg>
    </div>
  </header>

  <div class="value-bar">
    <span class="value-item"><svg width="30" height="30" viewBox="0 0 30 30"><path d="M3 14 L14 3 H26 V15 L15 26 Z" fill="none" stroke="#fff" stroke-width="2.5"/><circle cx="20" cy="9" r="2.5" fill="#fff"/></svg>Price Match Guarantee</span>
    <span class="value-item"><svg width="28" height="28" viewBox="0 0 28 28"><path d="M14 2 L26 8 V20 L14 26 L2 20 V8 Z" fill="#fff"/><path d="M2 8 L14 14 L26 8 M14 14 V26" stroke="#1351a8" stroke-width="2" fill="none"/></svg>Free Shipping</span>
    <span class="value-item"><svg width="30" height="30" viewBox="0 0 30 30"><circle cx="15" cy="15" r="12" fill="none" stroke="#fff" stroke-width="2.5"/><path d="M15 8 V15 L20 18" stroke="#fff" stroke-width="2.5" fill="none"/></svg>Same Day Service</span>
  </div>

  <section class="hero" role="img" aria-label="Photo of a man reading a book in front of library shelves">
    <h1 class="hero-title">ABOUT US</h1>
  </section>

  <section class="about">
    <h2 class="about-title">About Lesson Harbor</h2>
    <div class="about-rule"></div>
    <p class="about-copy">Your one stop place for [math curriculum] for both schools and homeschoolers.<br>Our price match guarantee, free shipping and same day service make us the perfect partner for all of your curriculum needs!Click here to see all of our [math] titles for grades 1-12 or select the grade you are looking for and you will find all of the available [math] products.</p>
  </section>

  <section class="latest">
    <h2 class="section-title"><span class="flourish left"></span>Latest Products<span class="flourish right"></span></h2>
    <div class="product-grid">
      <article class="product-card">
        <div class="product-cover cover-a" role="img" aria-label="Audio album cover with a portrait"></div>
        <p class="product-name">Bright Legends Volume 1 by Hearthside Tales®</p>
        <div class="price-row"><span class="price-old">$22</span><span class="price-new">$18</span><span class="buy-button">Buy Now</span></div>
      </article>
      <article class="product-card">
        <div class="product-cover cover-b" role="img" aria-label="Audio album cover with a painted scene"></div>
        <p class="product-name">Daring Voyages Volume 1 by Hearthside Tales®</p>
        <div class="price-row"><span class="price-old">$22</span><span class="price-new">$18</span><span class="buy-button">Buy Now</span></div>
      </article>
      <article class="product-card">
        <div class="product-cover cover-c" role="img" aria-label="Audio album cover with historical figures collage"></div>
        <p class="product-name">Bright Legends Volume 1 by Hearthside Tales®</p>
        <div class="price-row"><span class="price-old">$22</span><span class="price-new">$18</span><span class="buy-button">Buy Now</span></div>
      </article>
      <article class="product-card">
        <div class="product-cover cover-d" role="img" aria-label="Audio album cover with historical figures collage"></div>
        <p class="product-name">Daring Voyages Volume 1 by Hearthside Tales®</p>
        <div class="price-row"><span class="price-old">$22</span><span class="price-new">$18</span><span class="buy-button">Buy Now</span></div>
      </article>
    </div>
  </section>

  <section class="newsletter">
    <h2 class="newsletter-title">Subscribe to Our Newsletter</h2>
    <div class="newsletter-form"><span class="email-field">Email address</span><span class="subscribe-button">Subscribe</span></div>
  </section>

  <nav class="quick-links">
    <span class="quick-link"><svg width="34" height="34" viewBox="0 0 44 44" aria-label="Help"><circle cx="22" cy="22" r="20" fill="#fff"/><path d="M16 17 Q16 10 22 10 Q28 10 28 16 Q28 20 23 22 V26" stroke="#0f3d99" stroke-width="4" fill="none" stroke-linecap="round"/><circle cx="23" cy="33" r="2.6" fill="#0f3d99"/></svg></span>
    <span class="quick-link"><svg width="32" height="32" viewBox="0 0 44 44" aria-label="Settings"><circle cx="22" cy="22" r="13" fill="none" stroke="#fff" stroke-width="9" stroke-dasharray="5.1 5.1"/><circle cx="22" cy="22" r="11" fill="#fff"/><circle cx="22" cy="22" r="5" fill="#0f3d99"/></svg></span>
    <span class="quick-link"><svg width="34" height="34" viewBox="0 0 44 44" aria-label="Account"><circle cx="22" cy="13" r="10" fill="#fff"/><path d="M4 42 Q4 26 22 26 Q40 26 40 42 Z" fill="#fff"/></svg></span>
    <span class="quick-link"><svg width="30" height="30" viewBox="0 0 40 40" aria-label="Contact"><path d="M8 3 L15 3 L18 12 L13 16 Q17 24 24 27 L28 22 L37 25 L37 32 Q37 37 32 37 Q5 34 3 8 Q3 3 8 3 Z" fill="#fff"/></svg></span>
  </nav>

  <footer class="site-footer">
    <div class="social-row"><span class="social-dot"></span><span class="social-dot"></span><span class="social-dot"></span><span class="social-dot"></span><span class="social-dot"></span></div>
    <div class="payment-row"><span class="payment-card"></span><span class="payment-card"></span><span class="payment-card"></span><span class="payment-card"></span><span class="payment-card"></span></div>
    <p class="copyright">© 2017 Company Name &nbsp;All right reserved &nbsp;Term of Use</p>
  </footer>
</div>
</body>
</html>
```